Marlows Pet Care

Hi. I need a business card /logo for my pet care business. Im thinking about a dogs paw print. Although i do look after other pets so don't want to restrict my self. Open to suggestions on colour etc but like greens and purples.The name of my business is marlow's pet care. The logo could be just an image or have marlows power care on it. An option to do either would be great. For the winner i also would like a Web page (word press template if possible) designed if you can, of course I'll pay additional for this. Look forward to your ideas!

```html
<!DOCTYPE html>
<html lang="en">
<head>
<meta charset="utf-8">
<title>Marlow's Pet Care – Business Card</title>
<link rel="stylesheet" href="https://fonts.googleapis.com/css2?family=Cormorant+Garamond:ital,wght@1,700&display=swap">
<style>
  :root {
    --canvas: #ebe9ec;
    --brand-purple: #6a2c91;
    --wave-magenta: #b13c9e;
    --wave-violet: #5e2f8f;
    --wave-light: #d98fd0;
    --card-frost: #bdbac0;
    --ink: #141014;
  }
  html, body {
    margin: 0;
    padding: 0;
    overflow: hidden;
  }
  body {
    width: 1200px;
    height: 800px;
    background: var(--canvas);
    font-family: "Cormorant Garamond", Georgia, serif;
    font-style: italic;
    font-weight: 700;
    position: relative;
  }
  .brand-mark {
    position: absolute;
    top: 50px;
    left: 0;
    width: 1200px;
    display: flex;
    align-items: center;
    justify-content: center;
    gap: 24px;
    color: var(--brand-purple);
    font-size: 120px;
    line-height: 1;
  }
  .brand-dot {
    width: 46px;
    height: 46px;
    border-radius: 50%;
    background: var(--brand-purple);
  }
  .card-row {
    position: absolute;
    top: 300px;
    left: 60px;
    display: flex;
    gap: 60px;
  }
  .card {
    position: relative;
    width: 510px;
    height: 320px;
    border-radius: 16px;
    overflow: hidden;
  }
  .card svg {
    position: absolute;
    inset: 0;
  }
  .card-name {
    position: absolute;
    top: 26px;
    left: 28px;
    display: flex;
    align-items: center;
    gap: 12px;
    color: var(--brand-purple);
    font-size: 46px;
    line-height: 1;
  }
  .card-name .brand-dot {
    width: 18px;
    height: 18px;
  }
  .contact {
    position: absolute;
    right: 30px;
    bottom: 22px;
    margin: 0;
    text-align: right;
    color: var(--ink);
    font-size: 27px;
    line-height: 1.18;
    font-style: italic;
  }
  .contact .fb {
    color: #3a2550;
    opacity: 0.75;
  }
</style>
</head>
<body>
  <header class="brand-mark">
    <span class="brand-dot"></span>
    <span class="brand-name">Marlow's pet care</span>
  </header>

  <main class="card-row">
    <section class="card card-front" aria-label="Card front">
      <svg width="510" height="320" viewBox="0 0 510 320">
        <defs>
          <linearGradient id="front-wave" x1="0" y1="0" x2="1" y2="0.4">
            <stop offset="0" stop-color="var(--wave-magenta)"/>
            <stop offset="0.55" stop-color="#9a3aa0"/>
            <stop offset="1" stop-color="var(--wave-violet)"/>
          </linearGradient>
          <linearGradient id="front-trail" x1="0" y1="0" x2="1" y2="0">
            <stop offset="0" stop-color="var(--wave-light)" stop-opacity="0.15"/>
            <stop offset="0.5" stop-color="var(--wave-light)" stop-opacity="0.45"/>
            <stop offset="1" stop-color="var(--wave-light)" stop-opacity="0.1"/>
          </linearGradient>
        </defs>
        <rect class="card-frost" width="510" height="320" fill="var(--card-frost)"/>
        <path class="card-wave" d="M0,120 C150,100 300,70 510,60 L510,320 L0,320 Z" fill="url(#front-wave)"/>
        <path class="paw-trail" role="img" aria-label="Trail of paw prints across the wave"
              d="M0,235 C140,200 290,160 510,150 L510,185 C300,195 150,230 0,270 Z"
              fill="url(#front-trail)"/>
      </svg>
      <div class="card-name">
        <span class="brand-dot"></span>
        <span>Marlow's pet care</span>
      </div>
      <p class="contact">
        Marlow<br>
        017-555-0142<br>
        marlow@marlowspetcare.co.uk<br>
        <span class="fb">Fb name</span>
      </p>
    </section>

    <section class="card card-back" aria-label="Card back">
      <svg width="510" height="320" viewBox="0 0 510 320">
        <defs>
          <linearGradient id="back-wave" x1="0" y1="0" x2="1" y2="1">
            <stop offset="0" stop-color="var(--wave-violet)"/>
            <stop offset="0.6" stop-color="#9a3aa0"/>
            <stop offset="1" stop-color="var(--wave-magenta)"/>
          </linearGradient>
          <linearGradient id="back-trail" x1="0" y1="0" x2="1" y2="1">
            <stop offset="0" stop-color="var(--wave-light)" stop-opacity="0.15"/>
            <stop offset="0.5" stop-color="var(--wave-light)" stop-opacity="0.5"/>
            <stop offset="1" stop-color="var(--wave-light)" stop-opacity="0.15"/>
          </linearGradient>
        </defs>
        <rect class="card-frost" width="510" height="320" fill="var(--card-frost)"/>
        <path class="card-wave" d="M0,0 L250,0 C300,90 330,200 510,250 L510,320 L0,320 Z" fill="url(#back-wave)"/>
        <path class="card-band" d="M380,320 C420,290 470,280 510,280 L510,320 Z" fill="var(--wave-magenta)" opacity="0.7"/>
        <path class="paw-trail" role="img" aria-label="Trail of paw prints running down the wave"
              d="M170,0 L240,0 C280,100 320,220 420,320 L340,320 C250,220 210,110 170,0 Z"
              fill="url(#back-trail)"/>
      </svg>
    </section>
  </main>
</body>
</html>
```